Velvet corsaro

I want a business card design. the company is an infrastructure development company.

Target Market(s)

Government
real estate investors
real estate clients

Industry/Entity Type

Business

```html
<!DOCTYPE html>
<html lang="en">
<head>
<meta charset="utf-8">
<title>Velvet Corsaro – Business Card Options</title>
<link rel="stylesheet" href="https://fonts.googleapis.com/css2?family=Open+Sans:wght@300;400;600;700&display=swap">
<style>
  :root {
    --bg: #9a8878;
    --red: #e0262c;
    --red-soft: #ee8f8f;
    --red-deep: #b3161b;
    --blue: #1aa3e0;
    --paper: #f1f1f0;
    --ink: #111214;
    --option-one: #2aa6e6;
    --option-two: #e8343a;
  }
  * { box-sizing: border-box; margin: 0; padding: 0; }
  html, body { width: 1200px; height: 700px; overflow: hidden; }
  body {
    background: var(--bg);
    font-family: "Open Sans", Arial, sans-serif;
    position: relative;
  }
  .option-marker {
    position: absolute;
    border-radius: 50%;
    border: 1.5px solid;
    display: flex; align-items: center; justify-content: center;
    font-weight: 300;
  }
  .option-marker--one { left: -26px; top: 124px; width: 132px; height: 132px; border-color: var(--option-one); color: var(--option-one); font-size: 56px; }
  .option-marker--two { left: 571px; top: 116px; width: 148px; height: 148px; border-color: var(--option-two); color: var(--option-two); font-size: 60px; }

  .card {
    position: absolute;
    top: 222px;
    width: 468px; height: 268px;
    overflow: hidden;
  }
  .card--light { left: 72px; background: var(--paper); }
  .card--dark { left: 672px; background: var(--ink); border-radius: 18px; }

  .brand {
    position: absolute; left: 28px; top: 44px;
    display: flex; align-items: center; gap: 8px;
  }
  .brand__square { width: 14px; height: 14px; background: var(--blue); }
  .brand__name {
    color: var(--red); font-weight: 600; font-size: 19px; letter-spacing: 0.5px;
  }

  .holder {
    position: absolute; right: 28px; top: 150px;
    font-size: 17px; font-weight: 300; color: var(--blue);
  }
  .holder__first { font-weight: 700; }
  .card--light .holder__first { color: var(--red); }
  .card--dark .holder__first { color: var(--blue); }

  .contact-line {
    position: absolute; right: 28px; top: 180px;
    font-size: 9.3px; color: var(--blue); white-space: nowrap;
  }
  .contact-line b { font-weight: 700; }
  .card--dark .contact-line span.value { color: var(--blue); }
  .card--dark .contact-line .email-value { color: #7fbbd6; }

  .details {
    position: absolute; top: 210px; font-size: 6.8px; color: var(--red);
    line-height: 14px; text-transform: uppercase;
  }
  .details--office { left: 26px; }
  .details--phones { left: 218px; }
  .details--web { left: 318px; }
  .detail-row { display: flex; align-items: flex-start; gap: 8px; }
  .detail-row svg { width: 10px; height: 10px; margin-top: 2px; fill: var(--red); flex: none; }
  .office-title { font-weight: 700; }
  .card--dark .details { color: #c21e24; }

  .footer-band {
    position: absolute; left: 0; bottom: 0; width: 100%; height: 12px;
    display: flex;
  }
  .footer-band span { height: 100%; }
</style>
</head>
<body>

<div class="option-marker option-marker--one">1</div>
<div class="option-marker option-marker--two">2</div>

<!-- Option 1: light card -->
<section class="card card--light" aria-label="Business card, light version">
  <div class="brand"><span class="brand__square"></span><span class="brand__name">VELVET CORSARO</span></div>
  <p class="holder"><span class="holder__first">TUNDE</span> AFOLABI | MD</p>
  <p class="contact-line"><b>PHONE.</b> +234 8015550112 | <b>CELL.</b> +234 7015550467 | <b>EMAIL.</b> TUNDE@VELVETCORSARO.COM</p>

  <div class="details details--office">
    <div class="detail-row">
      <svg viewBox="0 0 10 10"><path d="M5 0a3.6 3.6 0 0 0-3.6 3.6C1.4 6.3 5 10 5 10s3.6-3.7 3.6-6.4A3.6 3.6 0 0 0 5 0zm0 5a1.4 1.4 0 1 1 0-2.8A1.4 1.4 0 0 1 5 5z"/></svg>
      <div><span class="office-title">Office</span><br>12, Adeyemi Street, off Allen Link Road<br>Ikeja Lagos, Nigeria</div>
    </div>
  </div>
  <div class="details details--phones">
    <div class="detail-row"><svg viewBox="0 0 10 10"><path d="M0 3c1-2 3-2.5 5-2.5S9 1 10 3L8 4 7 3H3L2 4zM2 5h6l1 4H1z"/></svg><span>+234 15550006</span></div>
    <div class="detail-row"><svg viewBox="0 0 10 10"><path d="M3 0h4a1 1 0 0 1 1 1v8a1 1 0 0 1-1 1H3a1 1 0 0 1-1-1V1a1 1 0 0 1 1-1zm0 1.5v6h4v-6z"/></svg><span>+234 7015550023</span></div>
  </div>
  <div class="details details--web">
    <div class="detail-row"><svg viewBox="0 0 10 10"><path d="M0 2h10v6H0zm1 .8V7h8V2.8L5 5.5z"/></svg><span>INFO@VELVETCORSARO.COM</span></div>
    <div class="detail-row"><svg viewBox="0 0 10 10"><path d="M5 0a5 5 0 1 0 0 10A5 5 0 0 0 5 0zm0 1c.8.8 1.3 2.2 1.4 3.5H3.6C3.7 3.2 4.2 1.8 5 1zM1 5.5h1.6c.1 1.2.4 2.3.9 3.1A4 4 0 0 1 1 5.5zm6.5 3.1c.5-.8.8-1.9.9-3.1H9a4 4 0 0 1-2.5 3.1z"/></svg><span>WWW.VELVETCORSARO.COM</span></div>
  </div>

  <div class="footer-band">
    <span style="width:28px;background:var(--red)"></span>
    <span style="width:18px;background:var(--red-deep)"></span>
    <span style="width:80px;background:var(--red-soft)"></span>
    <span style="width:288px;background:#f2a5a5"></span>
    <span style="width:30px;background:var(--red-deep)"></span>
    <span style="width:24px;background:var(--red)"></span>
  </div>
</section>

<!-- Option 2: dark card -->
<section class="card card--dark" aria-label="Business card, dark version">
  <div class="brand"><span class="brand__square"></span><span class="brand__name">VELVET CORSARO</span></div>
  <p class="holder"><span class="holder__first">TUNDE</span> AFOLABI | MD</p>
  <p class="contact-line"><b>PHONE.</b> <span class="value">+234 8015550112</span> | <b>CELL.</b> <span class="value">+234 7015550467</span> | <b>EMAIL.</b> <span class="email-value">TUNDE@VELVETCORSARO.COM</span></p>

  <div class="details details--office">
    <div class="detail-row">
      <svg viewBox="0 0 10 10"><path d="M5 0a3.6 3.6 0 0 0-3.6 3.6C1.4 6.3 5 10 5 10s3.6-3.7 3.6-6.4A3.6 3.6 0 0 0 5 0zm0 5a1.4 1.4 0 1 1 0-2.8A1.4 1.4 0 0 1 5 5z"/></svg>
      <div><span class="office-title">Office</span><br>12, Adeyemi Street, off Allen Link Road<br>Ikeja Lagos, Nigeria</div>
    </div>
  </div>
  <div class="details details--phones">
    <div class="detail-row"><svg viewBox="0 0 10 10"><path d="M0 3c1-2 3-2.5 5-2.5S9 1 10 3L8 4 7 3H3L2 4zM2 5h6l1 4H1z"/></svg><span>+234 15550006</span></div>
    <div class="detail-row"><svg viewBox="0 0 10 10"><path d="M3 0h4a1 1 0 0 1 1 1v8a1 1 0 0 1-1 1H3a1 1 0 0 1-1-1V1a1 1 0 0 1 1-1zm0 1.5v6h4v-6z"/></svg><span>+234 7015550023</span></div>
  </div>
  <div class="details details--web">
    <div class="detail-row"><svg viewBox="0 0 10 10"><path d="M0 2h10v6H0zm1 .8V7h8V2.8L5 5.5z"/></svg><span>INFO@VELVETCORSARO.COM</span></div>
    <div class="detail-row"><svg viewBox="0 0 10 10"><path d="M5 0a5 5 0 1 0 0 10A5 5 0 0 0 5 0zm0 1c.8.8 1.3 2.2 1.4 3.5H3.6C3.7 3.2 4.2 1.8 5 1zM1 5.5h1.6c.1 1.2.4 2.3.9 3.1A4 4 0 0 1 1 5.5zm6.5 3.1c.5-.8.8-1.9.9-3.1H9a4 4 0 0 1-2.5 3.1z"/></svg><span>WWW.VELVETCORSARO.COM</span></div>
  </div>
</section>

</body>
</html>
```